Verdant Rooms Stationary Set

Verdant Rooms is a bespoke interior design firm set to provide services to VIP clients with elegance and minimalism is the main theme for our stationary set. We require a full stationary set covering A4 letterhead, A4 & A3 envelopes, business cards, USB's, CDs, email signature and any other item the designer sees fit. logo is already designed and finalized, and we require the designer to use it as is without modifying the logo.

Address to be used on letterhead / business cards ...etc shall be as follows:

Phone : +971 2 518 3076
P.O. Box : 318947
Address: Block C&D, Bldg. 27, Court 14, Abu Dhabi, United Arab Emirates
Website: www.verdantrooms.example

Target Market(s)

VIP Clients

Industry/Entity Type

Interior Design

Font styles to use
Other font styles liked:
• something to be unique

Colors

Designer to choose colors to be used in the design.

Requirements
Must have
• Elegant, minimalistic
Nice to have
• Simple yet elegant design having a sharp yet clean cut format
Should not have
• No additional colours, just colours that are used in the logo (silver, black or gold)

```html
<!DOCTYPE html>
<html lang="en">
<head>
<meta charset="utf-8">
<title>Verdant Rooms – Business Cards</title>
<link href="https://fonts.googleapis.com/css2?family=Crimson+Text:wght@400;600&family=Dancing+Script:wght@600&display=swap" rel="stylesheet">
<style>
  :root {
    --backdrop: #1c1c1c;
    --card: #262525;
    --card-edge: #1a1a1a;
    --gold: #c9a447;
    --silver: #8d8d8d;
    --text-light: #e4e2dc;
    --text-muted: #a7a49c;
  }
  * { margin: 0; padding: 0; box-sizing: border-box; }
  html, body {
    width: 1200px; height: 800px; overflow: hidden;
    background: var(--backdrop);
  }
  .sheet {
    width: 1200px; height: 800px;
    display: flex; align-items: center; justify-content: center; gap: 60px;
  }
  .card {
    position: relative;
    width: 520px; height: 297px;
    background: var(--card);
    border: 1px solid var(--card-edge);
    box-shadow: 0 18px 40px rgba(0,0,0,0.45);
    font-family: "Crimson Text", Georgia, serif;
  }
  .brand-name {
    font-family: "Crimson Text", Georgia, serif;
    font-weight: 400;
    letter-spacing: 0.28em;
    text-transform: uppercase;
    white-space: nowrap;
  }
  .card-front .brand-name {
    position: absolute; left: 50%; top: 50%;
    transform: translate(-50%, -50%);
    font-size: 30px;
    color: var(--silver);
  }
  .card-back .brand-name {
    position: absolute; right: 36px; top: 52px;
    font-size: 24px;
    color: var(--gold);
  }
  .contact {
    position: absolute; left: 36px; bottom: 30px;
    color: var(--text-muted);
    font-size: 12.5px; line-height: 1.4;
  }
  .person-name {
    font-family: "Dancing Script", cursive;
    font-weight: 600;
    font-size: 24px;
    color: var(--gold);
    line-height: 1.1;
  }
  .person-title {
    color: var(--text-light);
    font-size: 15px;
    margin-bottom: 12px;
  }
  .address { margin-bottom: 12px; }
  .channels { list-style: none; }
  .channels li { display: flex; align-items: center; gap: 8px; }
  .channels svg { width: 10px; height: 10px; fill: var(--gold); flex: none; }
</style>
</head>
<body>
<main class="sheet">
  <section class="card card-front">
    <p class="brand-name">Verdant Rooms</p>
  </section>

  <section class="card card-back">
    <p class="brand-name">Verdant Rooms</p>
    <div class="contact">
      <p class="person-name">Daniel Hart</p>
      <p class="person-title">President</p>
      <p class="address">P.O. Box : 318947,<br>Block C&amp;D, Bldg. 27, Court 14<br>Abu Dhabi, United Arab Emirate</p>
      <ul class="channels">
        <li><svg viewBox="0 0 10 10" aria-hidden="true"><path d="M2 0.5 L3.6 0.5 L4.2 3 L3 3.8 Q4 6 6.2 7 L7 5.8 L9.5 6.4 L9.5 8 Q9.5 9.5 8 9.5 Q1 9 0.5 2 Q0.5 0.5 2 0.5 Z"/></svg>+971 2 518 3076</li>
        <li><svg viewBox="0 0 10 10" aria-hidden="true"><path d="M0.5 2 L9.5 2 L9.5 8 L0.5 8 Z M1 2.5 L5 5.5 L9 2.5" fill="var(--gold)" stroke="var(--card)" stroke-width="0.8"/></svg>info@verdantrooms.example</li>
        <li><svg viewBox="0 0 10 10" aria-hidden="true"><circle cx="5" cy="5" r="4.5"/><path d="M5 0.5 Q2.5 5 5 9.5 M5 0.5 Q7.5 5 5 9.5 M0.5 5 L9.5 5" fill="none" stroke="var(--card)" stroke-width="0.7"/></svg>www.verdantrooms.example</li>
      </ul>
    </div>
  </section>
</main>
</body>
</html>
```